Walk Bold Stay Kind Ebook and Print book cover

I need a professional, eye catching cover that will stand out. The title of the book is "Walk Bold Stay Kind: 47 Quiet Rules For Calm and Wonder" It is a self-help personal transformation book by author Dale Ormsby. The cover will be on both print and ebook covers. I want something that is similar yet different to best-selling books in the genre, nothing too boring. A blue background might work, but it isn't a requirement. I'm open to other colors as long as it's powerful, professional, and screams "Buy me because this book is going to change your life!"
Updates

So far, 3 designs (3 of the 4 star rated designs) are in contention, but they all can be improved. I think the book cover should best convey "thinking smart" in a dynamic way. I'll run another poll in a day or so when I get additional designs I like. Added Thursday, May 4, 2017

Based on current designs, I wanted to provide additional guidance. The title and image should pop and be clearly visible at a distance as a thumbnail. Also, I'm wanting something bold and creative but not too confusing. I currently have a couple solid designs that are in contention to win, but I have another 7 days left for the project. I extended it to 10 days from the initial 5. I'll include several more polls for my followers and will likely pick the top ranking design based off the series of polls and will be eliminating lower ranking designs with each new poll and set of promising designs that come in. Finally, I may ask to see what the back will look like on the print version since I'll need both the Lumora and print (5" by 8") designs. Added Saturday, May 6, 2017

It's been recommended by some that I should have my own picture on the cover. I'm not completely convinced, but I would like to see some additional designs that incorporate my photo (touched up to remove the shine from my forehead and the label brand name removed from the t-shire) into a cover design. I have several good designs coming in, so typeset and professional looking font is extremely important. Blue is also preferred but not required. I've attached the photo on the brief for those who want to submit a design with that photo. Added Saturday, May 6, 2017

Target Market(s)

Working age adults seeking personal transformation and self improvement.

Industry/Entity Type

Motivation

Requirements
Must have
• Creativity. Eye catching. Striking. Contrast. Looks good close up and as a thumbnail at a distance. Font should be easy to read and pop from the cover along with the design.
Nice to have
• Powerful image placement. Play up the "Walk Bold" aspect of the title. Perhaps even contrasting someone who's thinking "Hard." Here are a few examples of intriguing covers (though not necessarily related to the genre) I like mainly for aesthetics and creativity. https://www.shopvale.com/dp/Q71MRT2KWD/ https://www.shopvale.com/dp/Q34PLN8XEA
• https://www.shopvale.com/dp/Q925GHV3TC/
• https://www.shopvale.com/dp/Q48DJW6RZB/
• (the font is a little poor in the last one but the image is evoking)
Should not have
• Ugly, tacky, or hard to read fonts. A simple photo with text on top. A simple background with words. Confusing images. Designs with no additional stock image purchase requirements will be given preference over those that do. I've seen a lot of balloons and light bulbs. I'm not saying you can't include them in the design, but if you want to stand out, try to find something more creative that expresses the concept of the title.

```html
<!DOCTYPE html>
<html lang="en">
<head>
<meta charset="utf-8">
<title>Walk Bold Stay Kind — Dale Ormsby</title>
<link rel="stylesheet" href="https://fonts.googleapis.com/css2?family=Oranienbaum&display=swap">
<style>
  :root {
    --page-bg: #ffffff;
    --cover-teal: #0f3a44;
    --cover-teal-deep: #0a2d35;
    --title-white: #eef6f6;
    --title-yellow: #f2e64a;
    --cloud-pale: #e6f3f6;
    --cloud-shade: #c9e2e8;
    --bubble-ink: #123a44;
  }
  html, body {
    margin: 0;
    padding: 0;
    width: 1200px;
    height: 1137px;
    overflow: hidden;
    background: var(--page-bg);
  }
  .canvas {
    position: relative;
    width: 1200px;
    height: 1137px;
  }
  .cover {
    position: absolute;
    left: 320px;
    top: 48px;
    width: 560px;
    height: 1040px;
    background: radial-gradient(ellipse at 50% 40%, var(--cover-teal) 0%, var(--cover-teal-deep) 100%);
    overflow: hidden;
    font-family: "Oranienbaum", "Times New Roman", serif;
  }
  .title-top {
    position: absolute;
    left: 0;
    top: 22px;
    width: 100%;
    margin: 0;
    text-align: center;
    font-size: 112px;
    line-height: 1;
    font-weight: 400;
    color: var(--title-white);
    letter-spacing: 1px;
  }
  .title-link {
    position: absolute;
    left: 262px;
    top: 182px;
    margin: 0;
    font-size: 38px;
    line-height: 1;
    color: var(--title-yellow);
  }
  .title-bottom {
    position: absolute;
    left: 252px;
    top: 258px;
    margin: 0;
    font-size: 124px;
    line-height: 1;
    color: var(--title-yellow);
    letter-spacing: 2px;
  }
  .swing-illustration {
    position: absolute;
    left: 47px;
    top: 250px;
    width: 205px;
    height: 575px;
    border-radius: 100px 100px 20px 20px;
    background: linear-gradient(180deg, var(--cloud-pale) 0%, var(--cloud-shade) 18%, rgba(201,226,232,0.15) 30%, rgba(201,226,232,0.08) 100%);
  }
  .thought-bubble {
    position: absolute;
    left: 196px;
    top: 506px;
    width: 300px;
    height: 318px;
    border-radius: 48% 52% 50% 50%;
    background: radial-gradient(ellipse at 50% 45%, var(--cloud-pale) 60%, var(--cloud-shade) 100%);
  }
  .subtitle {
    position: absolute;
    left: 196px;
    top: 570px;
    width: 300px;
    margin: 0;
    text-align: center;
    color: var(--bubble-ink);
    line-height: 1.3;
  }
  .subtitle-number { display: block; font-size: 44px; line-height: 1.1; }
  .subtitle-line { display: block; font-size: 30px; }
  .subtitle-small { display: block; font-size: 24px; }
  .subtitle-caps { display: block; font-size: 26px; letter-spacing: 0.5px; }
  .author {
    position: absolute;
    left: 56px;
    top: 914px;
    margin: 0;
    font-size: 58px;
    line-height: 1;
    color: var(--title-white);
    letter-spacing: 2px;
  }
</style>
</head>
<body>
<main class="canvas">
  <article class="cover">
    <h1 class="title-top">WALK BOLD</h1>
    <p class="title-link">STAY</p>
    <p class="title-bottom">KIND</p>
    <div class="swing-illustration" role="img" aria-label="Illustration of a small white cloud with a child on a swing hanging from it"></div>
    <div class="thought-bubble" role="img" aria-label="Pale cloud-shaped thought bubble"></div>
    <p class="subtitle">
      <span class="subtitle-number">47</span>
      <span class="subtitle-line">Quiet Rules</span>
      <span class="subtitle-small">For</span>
      <span class="subtitle-caps">CALM &amp; WONDER</span>
    </p>
    <p class="author">DALE ORMSBY</p>
  </article>
</main>
</body>
</html>
```